Homemaking training schools needs a Business Card design

Designer, Hello!

No special requirements, good-looking enough.
--------------------------------------------------------------------------

Name: Marcus Liao
Chairman
Tel: 0574-57418263
Mobile: 13852247106
Email: kelvory@mailpond.com
Web: www.tqb2031.com
Add: No.258, LinfengJie, DaoyueQu, Ningbo, Zhejiang

LOGO
Ningbo TQB Homemaking Training School

Target Market(s)

pregnant women, mothers, infants, the elderly and families, including cleaning, cooking, nursing training.

Industry/Entity Type

Business

Contact Information for Business Card

Name: Marcus Liao
Chairman
Tel: 0574-57418263
Mobile: 13852247106
Email: kelvory@mailpond.com
Web: www.tqb2031.com

LOGO

Font styles to use
Serif
Sans Serif
Decorative

Requirements
Nice to have
• Feels: clean, specifications, safety, comfort, warmth and happiness.

```html
<!DOCTYPE html>
<html lang="en">
<head>
<meta charset="utf-8">
<title>TaoQiBang Business Card</title>
<link href="https://fonts.googleapis.com/css2?family=Didact+Gothic&family=Open+Sans:wght@600&display=swap" rel="stylesheet">
<style>
  :root {
    --stage: #e4e4e6;
    --paper: #f4f1ee;
    --edge: #d9673f;
    --ink: #2b2b2b;
    --muted: #6a6a6a;
    --rule: #b9b5b1;
  }
  * { box-sizing: border-box; margin: 0; padding: 0; }
  html, body { width: 1200px; height: 918px; overflow: hidden; }
  body {
    background: var(--stage);
    display: flex;
    align-items: center;
    justify-content: center;
    gap: 48px;
    font-family: "Open Sans", sans-serif;
    color: var(--ink);
  }
  .card {
    position: relative;
    width: 540px;
    height: 310px;
    background: var(--paper);
    border-bottom: 5px solid var(--edge);
    box-shadow: 0 6px 18px rgba(0,0,0,0.12);
  }
  .brand-name {
    position: absolute;
    font-family: "Open Sans", sans-serif;
    font-weight: 600;
    color: var(--ink);
    white-space: nowrap;
  }
  /* Front */
  .card--front .brand-name { left: 50%; top: 50%; transform: translate(-50%, -50%); font-size: 34px; }
  /* Back */
  .card--back .brand-name { left: 36px; top: 136px; font-size: 22px; }
  .person { position: absolute; left: 262px; top: 42px; width: 250px; border-bottom: 1px solid var(--rule); padding-bottom: 10px; }
  .person-name { font-family: "Didact Gothic", sans-serif; font-size: 32px; line-height: 1; }
  .person-title { font-family: "Didact Gothic", sans-serif; font-size: 13px; color: var(--muted); margin-top: 2px; }
  .contacts { position: absolute; left: 262px; top: 130px; list-style: none; font-size: 12.5px; line-height: 1.45; }
  .contact { display: flex; gap: 12px; margin-bottom: 12px; }
  .contact svg { flex: 0 0 14px; width: 14px; height: 14px; margin-top: 2px; fill: none; stroke: var(--ink); stroke-width: 1.6; }
  .contact svg.solid { fill: var(--ink); stroke: none; }
</style>
</head>
<body>
  <section class="card card--front">
    <span class="brand-name">TaoQiBang</span>
  </section>

  <section class="card card--back">
    <span class="brand-name">TaoQiBang</span>

    <div class="person">
      <div class="person-name">Marcus Liao</div>
      <div class="person-title">Chairman</div>
    </div>

    <ul class="contacts">
      <li class="contact">
        <svg class="solid" viewBox="0 0 14 14" aria-hidden="true"><path d="M7 0a5 5 0 0 0-5 5c0 3.6 5 9 5 9s5-5.4 5-9a5 5 0 0 0-5-5zm0 7a2 2 0 1 1 0-4 2 2 0 0 1 0 4z"/></svg>
        <span>No.258, LinfengJie, DaoyueQu,<br>Ningbo, Zhejiang</span>
      </li>
      <li class="contact">
        <svg class="solid" viewBox="0 0 14 14" aria-hidden="true"><path d="M3 1l2.2 2.6-1.2 1.6a8 8 0 0 0 4.8 4.8l1.6-1.2L13 11l-1.4 2C6 13 1 8 1 2.4z"/></svg>
        <span>0574-57418263<br>138 522 471 06</span>
      </li>
      <li class="contact">
        <svg viewBox="0 0 14 14" aria-hidden="true"><rect x="1" y="3" width="12" height="8"/><path d="M1 3l6 5 6-5"/></svg>
        <span>kelvory@mailpond.com</span>
      </li>
      <li class="contact">
        <svg viewBox="0 0 14 14" aria-hidden="true"><circle cx="7" cy="7" r="6"/><path d="M1 7h12M7 1c-3 3-3 9 0 12M7 1c3 3 3 9 0 12"/></svg>
        <span>tqb2031.com</span>
      </li>
    </ul>
  </section>
</body>
</html>
```